Business Card Admin Services

I have just selected a new logo. Now I need a business card.

The business is contract administrative services. We provide high value administrative services to small businesses/offices. We are professional, efficient, but also have fun and energetic personalities.

Lora Pike
Lora@DeskFalcon.ca
604-913-4078
DeskFalcon.ca

I will also want Facebook, Twitter and LinkedIn icons on the card - please up my "handles" beside each.
Facebook is DeskFalconCanada
Twitter is @DFalconLora
LinkedIn is LoraPikeDeskFalcon
Updates

New logo just updated.  Thanks for your patience!

Target Market(s)

Small businesses, professional offices

Industry/Entity Type

Business

Requirements
Must have
• bold, fun use of my colours
font needs to be consistent with the logo
Nice to have
• I quite like a closeup of the head

```html
<!DOCTYPE html>
<html lang="en">
<head>
<meta charset="utf-8">
<title>Desk Falcon – Business Card</title>
<link href="https://fonts.googleapis.com/css2?family=Open+Sans:wght@400;600;700&display=swap" rel="stylesheet">
<style>
  :root {
    --pink: #ee1a6e;
    --ink: #1d1d1b;
    --paper: #f1f1f3;
    --black: #000000;
    --white: #ffffff;
    --stage: #c8d5bf;
    --rule: #6d6d6d;
  }
  * { margin: 0; padding: 0; box-sizing: border-box; }
  html, body {
    width: 1200px; height: 849px; overflow: hidden;
    background: var(--stage);
    font-family: "Open Sans", Arial, sans-serif;
  }
  .card {
    position: absolute; left: 353px; width: 494px; height: 274px;
  }
  .card--front { top: 121px; background: var(--paper); }
  .card--back { top: 453px; background: var(--black); overflow: hidden; }

  .brand {
    position: absolute; display: flex; align-items: center;
  }
  .brand__name {
    font-weight: 700; color: var(--pink); letter-spacing: -0.5px;
  }
  .card--front .brand { right: 30px; top: 29px; gap: 10px; }
  .card--front .brand__name { font-size: 21px; }
  .brand__dot {
    width: 68px; height: 68px; border-radius: 50%; background: var(--pink);
  }

  .holder {
    position: absolute; left: 46px; top: 146px; right: 14px;
    display: flex; align-items: center; gap: 6px;
  }
  .holder__name {
    font-size: 17px; font-weight: 700; color: var(--pink); letter-spacing: 1px;
    white-space: nowrap;
  }
  .holder__rule {
    flex: 1; height: 2px; margin-top: 6px;
    background: linear-gradient(to right, var(--rule), rgba(109,109,109,0));
  }

  .contact, .social {
    position: absolute; list-style: none;
    font-size: 10px; color: var(--ink); letter-spacing: 1.4px;
  }
  .contact { left: 47px; top: 201px; line-height: 16px; }
  .social { left: 290px; top: 192px; line-height: 20px; letter-spacing: 0.6px; }
  .social li { display: flex; align-items: center; gap: 6px; }
  .social__mark {
    width: 14px; height: 14px; background: var(--pink); border-radius: 2px;
  }

  .mascot-closeup {
    position: absolute; left: 0; top: 0; width: 150px; height: 274px;
    background: radial-gradient(circle at 20% 40%, #ffffff 0 38%, #111 39% 100%);
  }
  .card--back .brand { left: 206px; top: 118px; }
  .card--back .brand__name { font-size: 31px; }
</style>
</head>
<body>
  <section class="card card--front" aria-label="Card front">
    <div class="brand">
      <span class="brand__name">DESKFALCON</span>
      <span class="brand__dot"></span>
    </div>
    <div class="holder">
      <span class="holder__name">Lora Pike</span>
      <span class="holder__rule"></span>
    </div>
    <ul class="contact">
      <li>604-913-4078</li>
      <li>Lora@DeskFalcon.ca</li>
      <li>www.DeskFalcon.ca</li>
    </ul>
    <ul class="social">
      <li><span class="social__mark"></span>@DFalconLora</li>
      <li><span class="social__mark"></span>DeskFalconCanada</li>
      <li><span class="social__mark"></span>LoraPikeDeskFalcon</li>
    </ul>
  </section>

  <section class="card card--back" aria-label="Card back">
    <div class="mascot-closeup" role="img" aria-label="Close-up illustration of the brand mascot's head with pink headband"></div>
    <div class="brand">
      <span class="brand__name">DESKFALCON</span>
    </div>
  </section>
</body>
</html>
```